Set of 6 Icons and buttons required

We have written a windows based app which gives clients access to reports etc.

We are a multichannel epos company

We require 6 buttons and icons along with a suggested font to use and a background for the form.

I have attatched a mock up of what we require from the chosen designer.

The buttons are as follows :

Stockcard ( This is a program which customers can enter stock and check stock levels etc )

Reports ( as the title says )

Stock ( This for making adjustments )

Goods ( this is for booking goods in )

Settings ( As title says )

Help ( As title says )

Dimensions
---------------

The form : 296x268
Buttons : 218x36
Icons on button : 32x32
Text size : Size 10

If you look at the attatched document this is something I put together just to show what we are looking once we put all the components together

Our website is q-lumora.co.uk

Target Market(s)

B2B

Industry/Entity Type

It Company

```html
<!DOCTYPE html>
<html lang="en">
<head>
<meta charset="utf-8">
<title>q-lumora – Launcher</title>
<link rel="stylesheet" href="https://fonts.googleapis.com/css2?family=Open+Sans:wght@400;700&display=swap">
<style>
  :root {
    --stage: #555555;
    --panel-dark: #231640;
    --panel-mid: #3a2766;
    --panel-light: #4a3580;
    --panel-edge: #14102a;
    --btn-top: #2a8ad6;
    --btn-bottom: #0b5da6;
    --btn-border: #0a3f73;
    --ink: #ffffff;
    --brand-ink: #f2f0f8;
    --home: #8fc6f2;
    --close: #8a8a8a;
    --mark-a: #2f6fb8;
    --mark-b: #0e2c5e;
  }
  * { box-sizing: border-box; margin: 0; padding: 0; }
  html, body { width: 1200px; height: 571px; overflow: hidden; }
  body {
    position: relative;
    background: var(--stage);
    font-family: "Open Sans", Verdana, sans-serif;
  }
  .launcher {
    position: absolute;
    left: 364px; top: 69px;
    width: 485px; height: 434px;
    border-radius: 10px;
    border: 2px solid var(--panel-edge);
    background: linear-gradient(160deg, var(--panel-dark) 0%, var(--panel-mid) 45%, var(--panel-light) 100%);
    box-shadow: 0 4px 14px rgba(0,0,0,.45);
  }
  .home-button {
    position: absolute; left: 8px; top: 6px;
    width: 28px; height: 26px;
  }
  .close-button {
    position: absolute; left: 461px; top: -18px;
    width: 32px; height: 32px;
  }
  .brand-name {
    position: absolute;
    left: 11px; top: 258px;
    width: 92px;
    text-align: center;
    font-size: 18px; font-weight: 700;
    color: var(--brand-ink);
    white-space: nowrap;
    line-height: 1.2;
  }
  .brand-square {
    position: absolute;
    left: 11px; top: 296px;
    width: 92px; height: 92px;
    border-radius: 6px;
    background: linear-gradient(135deg, var(--mark-a), var(--mark-b));
  }
  .menu {
    position: absolute; left: 114px; top: 29px;
    list-style: none;
  }
  .menu-button {
    display: flex; align-items: center;
    width: 353px; height: 56px;
    margin-bottom: 9px;
    border: 2px solid var(--btn-border);
    border-radius: 6px;
    background: linear-gradient(180deg, var(--btn-top), var(--btn-bottom));
    color: var(--ink);
    font-size: 23px; font-weight: 700;
  }
  .menu-icon { width: 46px; height: 46px; margin-left: 44px; flex: none; }
  .menu-label { margin-left: 96px; }
</style>
</head>
<body>
  <main class="launcher">
    <svg class="home-button" viewBox="0 0 28 26" aria-label="Home">
      <path d="M14 2 L27 13 H23 V25 H17 V17 H11 V25 H5 V13 H1 Z" fill="var(--home)"/>
    </svg>
    <svg class="close-button" viewBox="0 0 32 32" aria-label="Close">
      <circle cx="16" cy="16" r="15" fill="var(--close)" stroke="#cfcfcf" stroke-width="2"/>
      <path d="M10 10 L22 22 M22 10 L10 22" stroke="#ffffff" stroke-width="3.5" stroke-linecap="round"/>
    </svg>

    <div class="brand-name">q-lumora</div>
    <div class="brand-square"></div>

    <ul class="menu">
      <li class="menu-button">
        <svg class="menu-icon" viewBox="0 0 32 32" aria-hidden="true">
          <rect x="6" y="4" width="20" height="26" rx="2" fill="none" stroke="#fff" stroke-width="2.2"/>
          <rect x="11" y="2" width="10" height="5" rx="1" fill="#fff"/>
          <path d="M10 13 H22 M10 18 H22 M10 23 H22" stroke="#fff" stroke-width="2"/>
        </svg>
        <span class="menu-label">Stockcard</span>
      </li>
      <li class="menu-button">
        <svg class="menu-icon" viewBox="0 0 32 32" aria-hidden="true">
          <path d="M5 3 H18 L22 7 V15 M14 29 H5 Z" fill="none" stroke="#fff" stroke-width="2"/>
          <path d="M5 3 V29" stroke="#fff" stroke-width="2"/>
          <path d="M8 10 H17 M8 14 H14 M8 19 H12" stroke="#fff" stroke-width="1.8"/>
          <circle cx="20" cy="21" r="6" fill="none" stroke="#fff" stroke-width="2.6"/>
          <path d="M24.5 25.5 L30 31" stroke="#fff" stroke-width="3.4" stroke-linecap="round"/>
        </svg>
        <span class="menu-label">Reports</span>
      </li>
      <li class="menu-button">
        <svg class="menu-icon" viewBox="0 0 32 32" aria-hidden="true">
          <path d="M3 12 L16 8 L29 12 L16 16 Z" fill="#fff"/>
          <path d="M3 12 V24 L16 29 V16 Z" fill="#e6eef7"/>
          <path d="M29 12 V24 L16 29 V16 Z" fill="#fff"/>
          <path d="M9 9 L18 2 L27 6 L20 11 Z" fill="#fff" stroke="var(--btn-bottom)" stroke-width="1"/>
        </svg>
        <span class="menu-label">Stock</span>
      </li>
      <li class="menu-button">
        <svg class="menu-icon" viewBox="0 0 32 32" aria-hidden="true">
          <rect x="11" y="3" width="10" height="8" fill="#fff"/>
          <rect x="3" y="13" width="12" height="7" fill="#fff"/>
          <rect x="17" y="13" width="12" height="7" fill="#fff"/>
          <rect x="3" y="22" width="12" height="8" fill="#fff"/>
          <rect x="17" y="22" width="12" height="8" fill="#fff"/>
        </svg>
        <span class="menu-label">Goods</span>
      </li>
      <li class="menu-button">
        <svg class="menu-icon" viewBox="0 0 32 32" aria-hidden="true">
          <path d="M5 27 L19 13" stroke="#fff" stroke-width="4" stroke-linecap="round"/>
          <circle cx="22" cy="10" r="6" fill="#fff"/>
          <circle cx="25" cy="7" r="3" fill="var(--btn-top)"/>
          <path d="M27 27 L13 13" stroke="#fff" stroke-width="3.5" stroke-linecap="round"/>
          <rect x="4" y="5" width="12" height="6" rx="1" transform="rotate(45 10 8)" fill="#fff"/>
        </svg>
        <span class="menu-label">Settings</span>
      </li>
      <li class="menu-button">
        <svg class="menu-icon" viewBox="0 0 32 32" aria-hidden="true">
          <path d="M9 11 C9 5 23 4 23 11 C23 16 16 16 16 22" fill="none" stroke="#fff" stroke-width="4.5" stroke-linecap="round"/>
          <circle cx="16" cy="28" r="3" fill="#fff"/>
        </svg>
        <span class="menu-label">Help</span>
      </li>
    </ul>
  </main>
</body>
</html>
```